New Business Card Design for Business Consulting Business

We need a business card design that reflects the simplicity of our business. We partner with our clients to help them deliver change. We are a different kind of business consulting group. We don't just provide you with the theory. We provide you with the leadership and capability to execute change.

Vonduro is a professional services organisation that partners with their clients to lead the execution of strategic process and system improvement initiatives. Vonduro combines hands on delivery with coaching in best practice methodologies and approaches to build their clients capabilities to ensure their ongoing success in project implementations. Vonduro offers business advisory services in Project Management, Business Process Management, Change Management and Business Analytics.

Reason: Hi Designers, Thanks for all of your great designs. There are some really creative and cool ideas. Everyone is really capturing the essence of my business Vonduro. I am extending the deadline for the business card design by 6 days as I need to consult my Marketing colleague who won't be back in Australia until Wednesday. I would like to sit down with them and review all of the best designs. The key themes of the things I have really liked on my first review are: 1) Capturing the company website on the back of the card. 2) Including the company logo on the back of the card too. 3) Including the types of services on the back of the card that the company offers - Project Management - Business Process Management - Change Management - Business Analytics 4) Utilising some images on the back of the card Just so everyone knows the colour palette for the Vonduro company logo is: R: 0 G: 86 B: 162 or C: 97% M: 73% Y: 4% K: 0% Thanks Gareth

Hi Designers,

Thanks for all of your submissions to date.  I am working through each design and will provide feedback on all the great work.

One thing I would like to ask is if you could submit a version that has my academic credentials under or after my name.  I am not a big fan of doing this but as I am in business consulting it does seem to be quite common.

I hold a Bachelor of Commerce (BCom) and a Master of Business Administration (MBA)

Thanks

Gareth

Hi Designers,

Thanks for all of your fantastic designs.  There are some really great designs here for my business.  I am still in the process of reviewing designs and should have this completed by tomorrow.  Some of the things I have learnt from this round of designs are:

1) I prefer to have the card without my academic qualifications

2) I really like cards that have a blue back

3) I prefer to have my name and title either left or right of centre

I hope this helps and I will endeavour to get through all of the designs tomorrow

Cheers

Gareth

Target Market(s)

We target large corporate organisations

Industry/Entity Type

Leadership

Requirements
Must have
• Must have the following business details

Gareth Pilling - Director
Address: Level 7, 82 Harlow Street, Melbourne, Australia, 3000
Phone: +61 3 527 840 213
Fax: +61 3 9214 5037
Email: gareth.pilling@vonduro-example.com.au
LinkedIn: au.proflink-example.com/in/garethjpilling/
Twiiter: @garethjpilling
Website: www.vonduro-example.com.au

```html
<!DOCTYPE html>
<html lang="en">
<head>
<meta charset="utf-8">
<title>Vonduro Business Cards</title>
<link rel="stylesheet" href="https://fonts.googleapis.com/css2?family=Open+Sans:ital,wght@0,400;0,600;0,700;1,400&display=swap">
<style>
  :root {
    --brand-blue: #0056a2;
    --ink: #3a3a3a;
    --ink-soft: #555555;
    --paper: #ffffff;
    --backdrop: #eeeeee;
    --photo-dark: #3c3c3c;
    --photo-light: #d9d9d9;
  }
  * { box-sizing: border-box; margin: 0; padding: 0; }
  html, body { width: 1200px; height: 1200px; overflow: hidden; }
  body {
    background: var(--backdrop);
    font-family: "Open Sans", Arial, sans-serif;
    position: relative;
  }
  .card {
    position: absolute;
    left: 250px;
    width: 700px;
    height: 400px;
    background: var(--paper);
    box-shadow: 0 6px 18px rgba(0,0,0,0.12);
    overflow: hidden;
  }
  .card--front { top: 170px; }
  .card--back { top: 630px; }

  .wordmark {
    display: flex;
    align-items: center;
    gap: 10px;
    font-weight: 600;
    line-height: 1;
  }
  .wordmark__dot {
    width: 18px; height: 18px; border-radius: 50%;
    background: currentColor;
  }
  .wordmark__suffix {
    font-size: 11px;
    font-weight: 400;
    margin-top: 4px;
    text-align: right;
  }

  .front__logo {
    position: absolute; left: 34px; top: 30px;
    color: var(--brand-blue);
  }
  .front__logo .wordmark { font-size: 58px; }
  .front__band {
    position: absolute; left: 360px; right: 0; top: 118px; height: 56px;
    background: var(--brand-blue);
    border-radius: 28px 0 0 28px;
  }
  .front__address {
    position: absolute; left: 30px; top: 190px;
    display: flex; gap: 8px; font-style: normal;
    color: var(--ink); font-size: 15px; line-height: 1.35; font-weight: 600;
  }
  .front__address svg { flex: none; margin-top: 2px; }
  .front__person {
    position: absolute; right: 34px; top: 186px; text-align: right;
    color: var(--ink);
  }
  .person__name { font-size: 22px; font-weight: 700; }
  .person__role { font-weight: 400; color: var(--ink-soft); }
  .person__credentials { font-size: 12px; font-style: italic; color: var(--ink-soft); line-height: 1.35; }
  .front__contacts {
    position: absolute; right: 34px; top: 262px;
    list-style: none; text-align: right; color: var(--ink);
    font-size: 14px; line-height: 20px;
  }
  .front__contacts li { display: flex; justify-content: flex-end; align-items: center; gap: 8px; }
  .front__contacts .contact__web { font-weight: 700; font-size: 15px; }
  .contact__icon { width: 16px; height: 16px; flex: none; }

  .back__photo {
    position: absolute; inset: 0 0 70px 0;
    background: linear-gradient(150deg, var(--photo-dark) 0%, #8a8a8a 45%, var(--photo-light) 80%, var(--paper) 100%);
  }
  .back__fade {
    position: absolute; left: 0; right: 0; bottom: 0; height: 140px;
    background: linear-gradient(to bottom, rgba(255,255,255,0), var(--paper) 55%);
  }
  .back__tab {
    position: absolute; left: 0; top: 50px; width: 320px; height: 96px;
    background: var(--brand-blue); color: var(--paper);
    border-radius: 0 48px 48px 0;
    display: flex; align-items: center; padding-left: 34px;
  }
  .back__tab .wordmark { font-size: 54px; }
  .back__services {
    position: absolute; right: 30px; top: 180px;
    list-style: none; text-align: right;
    color: var(--brand-blue); font-size: 21px; line-height: 32px;
  }
  .back__services li { display: flex; justify-content: flex-end; align-items: center; gap: 10px; }
  .service__bullet {
    width: 14px; height: 14px; border-radius: 50%;
    border: 2px solid var(--brand-blue); background: var(--paper);
    display: flex; align-items: center; justify-content: center;
  }
  .service__bullet::after {
    content: ""; width: 6px; height: 6px; border-radius: 50%; background: var(--brand-blue);
  }
  .back__web {
    position: absolute; left: 34px; bottom: 26px;
    font-size: 24px; font-weight: 700; color: var(--ink);
  }
</style>
</head>
<body>

<section class="card card--front" aria-label="Business card front">
  <div class="front__logo">
    <div class="wordmark"><span>Vonduro</span><span class="wordmark__dot"></span></div>
    <div class="wordmark__suffix">Pty Ltd</div>
  </div>
  <div class="front__band"></div>

  <address class="front__address">
    <svg width="18" height="24" viewBox="0 0 18 24"><path d="M9 0C4 0 0 4 0 9c0 6 9 15 9 15s9-9 9-15c0-5-4-9-9-9z" fill="var(--brand-blue)"/><circle cx="9" cy="9" r="3.5" fill="#fff"/></svg>
    <span>Level 7, 82 Harlow Street,<br>Melbourne, Australia, 3000</span>
  </address>

  <div class="front__person">
    <p class="person__name">Gareth Pilling <span class="person__role">| Director</span></p>
    <p class="person__credentials">Bachelor of Commerce (BCom) -<br>Master of Business Administration (MBA)</p>
  </div>

  <ul class="front__contacts">
    <li>+61 3 527 840 213
      <svg class="contact__icon" viewBox="0 0 16 16"><circle cx="8" cy="8" r="8" fill="var(--brand-blue)"/><path d="M5 4l2 0 1 2.5-1.2 1a5 5 0 0 0 2 2l1-1.2 2.5 1v2c-4 .5-8-3.5-7.3-7.3z" fill="#fff"/></svg></li>
    <li>+61 3 9214 5037
      <svg class="contact__icon" viewBox="0 0 16 16"><circle cx="8" cy="8" r="8" fill="var(--brand-blue)"/><rect x="4" y="7" width="8" height="5" fill="#fff"/><rect x="5.5" y="4" width="5" height="3" fill="#fff"/></svg></li>
    <li>gareth.pilling@vonduro-example.com.au
      <svg class="contact__icon" viewBox="0 0 16 16"><circle cx="8" cy="8" r="8" fill="var(--brand-blue)"/><rect x="3.5" y="5" width="9" height="6" fill="#fff"/><path d="M3.5 5l4.5 3.5 4.5-3.5" stroke="var(--brand-blue)" fill="none"/></svg></li>
    <li>au.proflink-example.com/in/garethjpilling/
      <svg class="contact__icon" viewBox="0 0 16 16"><circle cx="8" cy="8" r="8" fill="var(--brand-blue)"/></svg></li>
    <li>@garethjpilling
      <svg class="contact__icon" viewBox="0 0 16 16"><circle cx="8" cy="8" r="8" fill="var(--brand-blue)"/></svg></li>
    <li class="contact__web">www.vonduro-example.com.au
      <svg class="contact__icon" viewBox="0 0 16 16"><circle cx="8" cy="8" r="8" fill="var(--brand-blue)"/><circle cx="8" cy="8" r="5" fill="none" stroke="#fff"/><ellipse cx="8" cy="8" rx="2" ry="5" fill="none" stroke="#fff"/><path d="M3 8h10" stroke="#fff"/></svg></li>
  </ul>
</section>

<section class="card card--back" aria-label="Business card back">
  <div class="back__photo" role="img" aria-label="Black and white photograph of two businesspeople shaking hands"></div>
  <div class="back__fade"></div>
  <div class="back__tab">
    <div>
      <div class="wordmark"><span>Vonduro</span><span class="wordmark__dot"></span></div>
      <div class="wordmark__suffix">Pty Ltd</div>
    </div>
  </div>
  <ul class="back__services">
    <li>Business Process Management <span class="service__bullet"></span></li>
    <li>Project Management <span class="service__bullet"></span></li>
    <li>Change Management <span class="service__bullet"></span></li>
    <li>Business Analytics <span class="service__bullet"></span></li>
  </ul>
  <p class="back__web">www.vonduro-example.com.au</p>
</section>

</body>
</html>
```